THE HEADLAND AT TALL PINE HUDSON RIVER WATERFRONT LAND

crisp clear business cards on wood stock or thick paper with large font with a river otter logo, PERSONAL INFO ON ONE SIDE, PROJECT INFO ON THE OTHER SIDE
Updates

I don’t have a logo. Just thought that a photo of a river otter would look appealing.

Target Market(s)

Buyers and realtors

Industry/Entity Type

Real Estate Development

Contact Information for Business Card

MARTIN KOWALCZYK
607-318-5942 (Call or Text)
STONE MEADOW LLC PRINCIPAL

RQVWFIELD@NORVAMAIL.NET

Font styles to use
Sans Serif

Colors
fbfdfe
0792cd
00a990
fbed22
ec1f27

Requirements
Must have
• LARGE FONT, ROUNDED EDGES,
Nice to have
• ON THE BACK SIDE :
• THE HEADLAND AT TALL PINE
• HUDSON RIVER WATERFRONT LAND
• 2 TO 67 ACRES---READY TO BUILD
• PRICED TO SELL!

```html
<!DOCTYPE html>
<html lang="en">
<head>
<meta charset="utf-8">
<title>The Headland at Tall Pine – Business Card</title>
<link rel="stylesheet" href="https://fonts.googleapis.com/css2?family=Montserrat:wght@300;400;500;700;800&display=swap">
<style>
  :root {
    --backdrop: #e9e6e1;
    --card-white: #ffffff;
    --card-blue: #3b58a8;
    --ink: #111111;
    --accent-blue: #3b58a8;
    --on-blue: #ffffff;
    --photo-dark: #3c3a36;
    --photo-mid: #6b6a63;
    --photo-green: #3f7a3a;
  }
  * { box-sizing: border-box; margin: 0; padding: 0; }
  html, body { width: 900px; height: 1200px; overflow: hidden; }
  body {
    background: var(--backdrop);
    font-family: "Montserrat", sans-serif;
    position: relative;
  }
  .card {
    position: absolute;
    left: 85px;
    width: 733px;
    height: 429px;
    border-radius: 24px;
    overflow: hidden;
    box-shadow: 0 6px 14px rgba(0,0,0,0.25);
  }
  .card-front { top: 143px; background: var(--card-white); }
  .card-back { top: 633px; background: var(--card-blue); color: var(--on-blue); text-align: center; }

  .name-band {
    position: absolute; top: 65px; left: 0; right: 0; height: 79px;
    background: var(--card-blue);
    display: flex; align-items: center; padding-left: 45px;
  }
  .name { color: var(--on-blue); font-weight: 700; font-size: 30px; letter-spacing: 0.3px; }
  .project-title {
    position: absolute; top: 160px; left: 45px;
    font-weight: 700; font-size: 35px; color: var(--ink); letter-spacing: 0.5px;
  }
  .company { position: absolute; top: 242px; left: 45px; font-weight: 700; font-size: 26px; color: var(--ink); }
  .role { position: absolute; top: 279px; left: 45px; font-weight: 500; font-size: 20px; color: var(--accent-blue); }
  .phone { position: absolute; top: 316px; left: 45px; font-weight: 700; font-size: 26px; color: var(--ink); }
  .phone-note { color: var(--accent-blue); font-weight: 500; }
  .email { position: absolute; top: 362px; left: 45px; font-weight: 700; font-size: 22px; color: var(--ink); }

  .otter-photo { position: absolute; top: 35px; left: 287px; width: 160px; height: 160px; }
  .photo-caption { position: absolute; top: 205px; left: 0; right: 0; font-size: 16px; font-weight: 400; }
  .pitch { position: absolute; top: 236px; left: 0; right: 0; font-size: 30px; line-height: 41px; }
  .pitch-line { display: block; }
  .light { font-weight: 300; }
  .bold { font-weight: 800; font-size: 31px; }
</style>
</head>
<body>
  <section class="card card-front">
    <div class="name-band"><span class="name">MARTIN KOWALCZYK</span></div>
    <h1 class="project-title">THE HEADLAND AT TALL PINE</h1>
    <p class="company">STONE MEADOW LLC</p>
    <p class="role">PRINCIPAL</p>
    <p class="phone">607-318-5942 <span class="phone-note">(CALL OR TEXT)</span></p>
    <p class="email">RQVWFIELD@NORVAMAIL.NET</p>
  </section>

  <section class="card card-back">
    <svg class="otter-photo" viewBox="0 0 160 160" role="img" aria-label="Photo of a Hudson River otter">
      <defs>
        <radialGradient id="otterTones" cx="50%" cy="45%" r="60%">
          <stop offset="0%" stop-color="var(--photo-mid)"/>
          <stop offset="70%" stop-color="var(--photo-dark)"/>
          <stop offset="100%" stop-color="var(--photo-green)"/>
        </radialGradient>
      </defs>
      <circle cx="80" cy="80" r="77" fill="none" stroke="var(--on-blue)" stroke-width="3"/>
      <circle cx="80" cy="80" r="69" fill="url(#otterTones)"/>
    </svg>
    <p class="photo-caption">Hudson River Otter</p>
    <p class="pitch">
      <span class="pitch-line light">THE HEADLAND AT TALL PINE</span>
      <span class="pitch-line bold">HUDSON RIVER WATERFRONT LAND</span>
      <span class="pitch-line"><span class="bold">2 TO 67 ACRES</span><span class="light">---READY TO BUILD</span></span>
      <span class="pitch-line light">PRICED TO SELL!</span>
    </p>
  </section>
</body>
</html>
```